private relaxation massage therapist business card

I want a card that does not give a physical address as I am able to massage at home as well as be mobile. I want on the back somewhere to put appointment details and also my bank acct details for payment being to acct 38 7402 0061948 00
I have a Certificate in Relaxation Massage from KPTA 2014
I would like to use blue colours and maybe have some fluffy clouds somewhere on the business card.

Industry/Entity Type

Massage

Contact Information for Business Card

Fiona Marsh
Relaxation Massage Therapist

telephone 0216 842 197 or 09 4718335
email fionamarsh72@quellbox.com

Requirements
Must have
• bold lettering, lots of white space, On the reverse of the card some lines in a box for me to write appointment times also on reverse my bank acct details for payment on line.

```html
<!DOCTYPE html>
<html lang="en">
<head>
<meta charset="utf-8">
<title>Fiona Marsh – Appointment Card</title>
<link href="https://fonts.googleapis.com/css2?family=Jost:wght@400;500&display=swap" rel="stylesheet">
<style>
  :root {
    --sky-deep: #8eeaf0;
    --sky-mid: #b4f4f6;
    --sky-light: #e2fcfd;
    --ink-name: #1467ee;
    --ink: #1a80f2;
    --paper: #ffffff;
    --slip: rgba(240, 253, 254, 0.92);
    --slip-edge: #9a9a6a;
  }
  * { margin: 0; padding: 0; box-sizing: border-box; }
  html, body { width: 1200px; height: 741px; overflow: hidden; }
  body { font-family: "Jost", "Futura", sans-serif; color: var(--ink); }

  .card {
    position: relative;
    width: 1200px;
    height: 741px;
    overflow: hidden;
    background:
      radial-gradient(ellipse 420px 260px at 1080px 70px, rgba(255,255,255,0.55), transparent 70%),
      radial-gradient(ellipse 380px 240px at 80px 120px, rgba(255,255,255,0.35), transparent 70%),
      radial-gradient(ellipse 520px 300px at 620px 720px, rgba(255,255,255,0.45), transparent 70%),
      radial-gradient(ellipse 360px 260px at 1150px 520px, rgba(255,255,255,0.35), transparent 70%),
      linear-gradient(160deg, var(--sky-deep) 0%, var(--sky-mid) 45%, var(--sky-light) 100%);
  }

  .therapist-name {
    position: absolute; left: 0; right: 0; top: 38px;
    text-align: center;
    font-size: 55px; font-weight: 400; line-height: 1;
    color: var(--ink-name);
  }
  .credential {
    position: absolute; left: 0; right: 0; top: 115px;
    text-align: center;
    font-size: 30px; font-weight: 400; line-height: 1;
  }

  .appointment-panel {
    position: absolute; left: 86px; top: 168px;
    width: 1028px; height: 324px;
    background: var(--paper);
  }
  .appointment-title {
    position: absolute; left: 0; right: 0; top: 15px;
    text-align: center;
    font-size: 39px; font-weight: 500; line-height: 1;
  }
  .field-label {
    position: absolute;
    font-size: 42px; line-height: 1;
  }
  .write-line {
    position: absolute; height: 0;
    border-bottom: 2px dotted var(--ink);
  }
  .meridiem {
    position: absolute;
    font-size: 30px; line-height: 1;
  }

  .payment-slip {
    position: absolute; left: 235px; top: 521px;
    width: 725px; height: 138px;
    background: var(--slip);
    box-shadow: 0 4px 14px rgba(40, 120, 140, 0.25);
    text-align: center;
  }
  .slip-edge {
    position: absolute; top: 500px; width: 2px; height: 181px;
    background: linear-gradient(to bottom, transparent, var(--slip-edge) 30%, var(--slip-edge) 70%, transparent);
    opacity: 0.7;
  }
  .payment-note {
    position: absolute; left: 0; right: 0; top: 29px;
    font-size: 32px; line-height: 1;
  }
  .account-line {
    position: absolute; left: 0; right: 0; top: 84px;
    font-size: 33px; line-height: 1;
  }
  .account-number { font-weight: 500; font-size: 35px; }
</style>
</head>
<body>
  <main class="card">
    <h1 class="therapist-name">Fiona Marsh</h1>
    <p class="credential">Certified Relaxation Massager (KPTA 2014)</p>

    <section class="appointment-panel">
      <h2 class="appointment-title">APPOINTMENT</h2>

      <span class="field-label" style="left:37px; top:128px;">For</span>
      <span class="write-line" style="left:116px; top:160px; width:870px;"></span>

      <span class="field-label" style="left:31px; top:248px;">On</span>
      <span class="write-line" style="left:112px; top:280px; width:478px;"></span>
      <span class="field-label" style="left:600px; top:248px;">At</span>
      <span class="write-line" style="left:660px; top:280px; width:214px;"></span>
      <span class="meridiem" style="left:876px; top:258px;">AM/PM</span>
    </section>

    <span class="slip-edge" style="left:234px;"></span>
    <span class="slip-edge" style="left:959px;"></span>
    <section class="payment-slip">
      <p class="payment-note">Please Pay Online to</p>
      <p class="account-line">A/c No : <span class="account-number">38 7402 0061948 00</span></p>
    </section>
  </main>
</body>
</html>
```